Brimovex business card

Based on company logo and website given , to design a business card temple. Slogan "Your furry friends deserves the best"
Color style please refer to our website

```html
<!DOCTYPE html>
<html lang="en">
<head>
<meta charset="utf-8">
<title>Brimovex business card</title>
<link href="https://fonts.googleapis.com/css2?family=Arimo&family=Bebas+Neue&family=Tinos&display=swap" rel="stylesheet">
<style>
  :root {
    --backdrop: #2b2b2d;
    --card: #1d1e20;
    --gold: #c4b22f;
    --text-light: #dcdcdc;
    --rule: #55565a;
    --white: #ffffff;
    --photo-top: #2a3a1a;
    --photo-bottom: #6f932f;
  }
  html, body {
    margin: 0;
    width: 1200px;
    height: 1108px;
    overflow: hidden;
    background: var(--backdrop);
  }
  .canvas {
    position: relative;
    width: 1200px;
    height: 1108px;
  }
  .card {
    position: absolute;
    top: 224px;
    width: 400px;
    height: 660px;
    background: var(--card);
    border-radius: 22px;
    overflow: hidden;
    box-shadow: 0 12px 30px rgba(0,0,0,0.45);
  }
  .card--front { left: 150px; }
  .card--back { left: 650px; }

  .brand {
    position: absolute;
    top: 120px;
    left: 0;
    right: 0;
    text-align: center;
    font-family: "Tinos", serif;
    font-size: 92px;
    color: var(--gold);
    letter-spacing: -2px;
  }
  .person {
    position: absolute;
    top: 330px;
    left: 0;
    right: 0;
    text-align: center;
  }
  .person__name {
    font-family: "Tinos", serif;
    font-size: 27px;
    color: var(--gold);
    letter-spacing: 1px;
    margin: 0;
  }
  .person__role {
    font-family: "Arimo", sans-serif;
    font-size: 19px;
    color: var(--text-light);
    margin: 2px 0 0;
  }
  .icon-row {
    position: absolute;
    top: 404px;
    left: 30px;
    right: 30px;
    display: flex;
    align-items: center;
    justify-content: center;
    gap: 6px;
  }
  .icon-row__rule {
    flex: 1;
    height: 1px;
    background: var(--rule);
    margin: 0 4px;
  }
  .icon {
    width: 32px;
    height: 32px;
    border-radius: 6px;
    background: var(--gold);
    display: flex;
    align-items: center;
    justify-content: center;
  }
  .contact {
    position: absolute;
    top: 452px;
    left: 0;
    right: 0;
    text-align: center;
    font-family: "Arimo", sans-serif;
    font-size: 20px;
    line-height: 26px;
    color: var(--text-light);
  }
  .contact p { margin: 0; }
  .contact__rule {
    width: 200px;
    height: 1px;
    background: var(--rule);
    margin: 12px auto 14px;
  }

  .photo {
    position: absolute;
    top: 0;
    left: 0;
    width: 400px;
    height: 378px;
    background: linear-gradient(180deg, var(--photo-top) 0%, var(--photo-bottom) 100%);
  }
  .slogan {
    position: absolute;
    top: 430px;
    left: 0;
    right: 0;
    text-align: center;
    font-family: "Bebas Neue", sans-serif;
    font-size: 52px;
    line-height: 56px;
    color: var(--white);
    margin: 0;
    letter-spacing: 0.5px;
  }
</style>
</head>
<body>
<div class="canvas">

  <section class="card card--front">
    <div class="brand">Brimovex</div>

    <div class="person">
      <p class="person__name">MARCUS HALE</p>
      <p class="person__role">Managing Director</p>
    </div>

    <div class="icon-row">
      <span class="icon-row__rule"></span>
      <span class="icon" aria-label="Phone">
        <svg width="20" height="20" viewBox="0 0 20 20"><path d="M3 7c0-2 3-3 7-3s7 1 7 3l-3 1-1-2H7L6 8z M5 9h10l1 7H4z" fill="#1d1e20"/></svg>
      </span>
      <span class="icon" aria-label="Mobile">
        <svg width="20" height="20" viewBox="0 0 20 20"><rect x="6" y="2" width="8" height="16" rx="1.5" fill="#1d1e20"/><rect x="7.5" y="4" width="5" height="10" fill="#c4b22f"/></svg>
      </span>
      <span class="icon" aria-label="Website">
        <svg width="20" height="20" viewBox="0 0 20 20"><circle cx="10" cy="10" r="7.5" fill="#1d1e20"/><path d="M2.5 10h15M10 2.5c-3 3-3 12 0 15M10 2.5c3 3 3 12 0 15" stroke="#c4b22f" stroke-width="1.2" fill="none"/></svg>
      </span>
      <span class="icon" aria-label="Email">
        <svg width="20" height="20" viewBox="0 0 20 20"><rect x="2.5" y="5" width="15" height="10" fill="none" stroke="#1d1e20" stroke-width="1.6"/><path d="M2.5 5l7.5 6 7.5-6" stroke="#1d1e20" stroke-width="1.4" fill="none"/></svg>
      </span>
      <span class="icon-row__rule"></span>
    </div>

    <div class="contact">
      <p>+61 3 9460 2218</p>
      <p>1800 317 644</p>
      <p>www.brimovex.com.au</p>
      <p>sales@brimovex.com.au</p>
      <div class="contact__rule"></div>
      <p>9/42 Larkfield Road</p>
      <p>Glen Ardell Vic 3152</p>
    </div>
  </section>

  <section class="card card--back">
    <div class="photo" role="img" aria-label="Photo of a puppy and a kitten sitting together on a grassy lawn"></div>
    <p class="slogan">Your furry friends<br>deserves the best</p>
  </section>

</div>
</body>
</html>
```